Belmorin InsurTech Website Redesign - 10 Pages

Design a modern, professional website for Belmorin, an AI-native cyber insurance platform serving SMBs.

DELIVERABLE: 10 pages (desktop + mobile mockups)
- Homepage (priority #1)
- 4 Platform pages (Cyber Insurance, Brokers, Underwriters, Policyholder)
- 3 Company pages (About Us, Team, Contact/Careers)
- 2 Risk pages (AI Risk, Cyber Risk)

DESIGN DIRECTION:
- Professional + innovative (insurance meets technology)
- Trust-building + modern aesthetic
- Reference: Pellbrook Insurance, Driftmoor Insurance
- Use official brand colors (6-color palette provided)
- Avoid generic security clipart (padlocks, shields, magnifying glasses)
- Custom graphics, not AI-generated or stock imagery

CURRENT SITES FOR REFERENCE:
- www.belmorin-cover.test
- https://a3c9140d.belmorin-website.previewhost.test/

Full detailed brief with all content, page specifications, and brand guidelines attached as PDF (Belmorin_MockupLane_Brief.pdf).

TARGET AUDIENCE: Insurance brokers (primary), SMB business owners (secondary)
KEY MESSAGE: "Cyber Insurance the Way It Should Be"

Additional brand assets available in Google Drive - link provided on request.

```html
<!DOCTYPE html>
<html lang="en">
<head>
<meta charset="UTF-8">
<title>Belmorin — Cyber Insurance the Way It Should Be</title>
<link href="https://fonts.googleapis.com/css2?family=Poppins:wght@500;600;700&family=Inter:wght@400;500;600&display=swap" rel="stylesheet">
<style>
:root{
  --navy:#161a45;
  --blue:#1f1ff0;
  --blue-deep:#1a14c8;
  --mint:#5fdcb4;
  --mint-soft:#8fe3cc;
  --teal-dark:#0f3d3b;
  --footer:#0d3836;
  --text:#26283a;
  --line:#c9cdf0;
}
*{margin:0;padding:0;box-sizing:border-box}
html,body{width:1200px;height:4258px;overflow:hidden}
body{position:relative;background:#fff;font-family:"Inter",Arial,sans-serif;color:var(--text)}
.abs{position:absolute}
.accent{color:var(--blue)}

/* header + hero */
.hero{position:absolute;left:0;top:0;width:1200px;height:719px;
  background:
    radial-gradient(ellipse 520px 420px at 120px 330px,rgba(140,230,190,.45),transparent 70%),
    radial-gradient(ellipse 600px 520px at 1080px 460px,rgba(170,175,245,.55),transparent 70%),
    linear-gradient(90deg,#e6f8ef,#f3f5fc 50%,#e7e8fb);}
.brand{position:absolute;display:flex;align-items:center;gap:12px;font-family:"Poppins",Arial,sans-serif;font-weight:600;letter-spacing:.5px}
.brand .mark{width:26px;height:26px;background:var(--blue);border-radius:4px}
.site-brand{left:99px;top:20px;font-size:34px;color:var(--blue)}
.nav-link{position:absolute;top:32px;font-family:"Poppins",Arial,sans-serif;font-size:14px;font-weight:500;color:var(--navy);text-decoration:none;white-space:nowrap}
.btn-nav{position:absolute;left:1003px;top:26px;width:119px;height:34px;border-radius:17px;background:var(--mint-soft);color:#fff;font-family:"Poppins",Arial,sans-serif;font-size:14px;font-weight:500;display:flex;align-items:center;justify-content:center;gap:6px}
.hero-title{left:113px;top:222px;font-family:"Poppins",Arial,sans-serif;font-weight:600;font-size:48px;line-height:64px;color:var(--navy)}
.hero-sub{left:118px;top:362px;font-size:22px;line-height:31px;color:var(--text)}
.btn{position:absolute;display:flex;align-items:center;justify-content:center;gap:8px;background:var(--blue);color:#fff;border-radius:24px;font-weight:600;font-size:16px}
.tri{width:0;height:0;border-left:7px solid transparent;border-right:7px solid transparent;border-top:11px solid #fff}
.hero-art{left:595px;top:80px;width:520px;height:560px;border-radius:40px;
  background:radial-gradient(ellipse 240px 140px at 50% 25%,rgba(42,47,240,.75),transparent 75%),
             radial-gradient(ellipse 140px 200px at 50% 70%,rgba(120,235,170,.7),transparent 75%)}
.tag{position:absolute;background:#fff;border-radius:6px;box-shadow:0 4px 14px rgba(40,50,120,.12);font-size:13px;font-weight:600;color:var(--navy);padding:10px 14px;line-height:15px}

/* section headings */
.sec-title{position:absolute;left:0;width:1200px;text-align:center;font-family:"Poppins",Arial,sans-serif;font-weight:600;font-size:36px;color:var(--navy);line-height:46px}
.underline{position:absolute;width:80px;height:3px;left:560px;background:linear-gradient(90deg,var(--mint) 0 40%,var(--blue) 40%)}

/* features */
.f-title{position:absolute;font-family:"Poppins",Arial,sans-serif;font-weight:500;font-size:30px;line-height:35px;color:#111}
.f-bar{position:absolute;width:60px;height:3px;background:linear-gradient(90deg,var(--mint) 0 40%,var(--blue) 40%)}
.f-text{position:absolute;font-size:18.5px;line-height:31px;color:#333}
.art{position:absolute;border-radius:24px}

/* lifecycle */
.lifecycle{position:absolute;left:0;top:2400px;width:1200px;height:675px;background:linear-gradient(180deg,#eef0fa 0%,#f2f3fb 60%,#eef0f8 100%)}
.floor{position:absolute;left:0;top:2930px;width:1200px;height:145px;background:linear-gradient(180deg,rgba(210,214,238,0),rgba(200,205,235,.55))}
.step{position:absolute;width:150px;text-align:center}
.step h3{font-family:"Poppins",Arial,sans-serif;font-weight:600;font-size:18px;color:#111;letter-spacing:.3px}
.step p{font-size:11.5px;line-height:14px;color:#333;margin-top:14px}

/* integrations */
.integrations{position:absolute;left:0;top:3075px;width:1200px;height:724px;
  background:
    radial-gradient(ellipse 500px 380px at 1100px 620px,rgba(170,175,245,.5),transparent 70%),
    radial-gradient(ellipse 420px 320px at 40px 620px,rgba(150,230,200,.45),transparent 70%),
    #fbfcfe}
.tab{position:absolute;left:131px;width:262px;height:55px;display:flex;align-items:center;padding-left:32px;font-family:"Poppins",Arial,sans-serif;font-weight:600;font-size:18px;color:var(--blue-deep)}
.tab.active{background:linear-gradient(90deg,var(--blue),#2a3ff0 70%,#7fe0c8);color:#fff;border-radius:6px 0 0 6px}
.int-card{position:absolute;left:393px;top:3311px;width:662px;height:359px;background:#fff;border:1px solid #e1e4f2;border-radius:4px;box-shadow:0 8px 30px rgba(60,70,140,.08)}
.int-card h4{position:absolute;left:38px;top:46px;font-family:"Poppins",Arial,sans-serif;font-weight:600;font-size:21px;color:var(--blue-deep)}
.logo-box{position:absolute;top:102px;width:189px;height:146px;border:1px solid #dadde8;border-radius:3px;display:flex;align-items:center;justify-content:center;font-family:"Poppins",Arial,sans-serif;font-weight:500;font-size:20px;color:#3a3d4f;text-align:center}

/* footer */
.footer{position:absolute;left:0;top:3799px;width:1200px;height:459px;background:var(--footer);color:#fff}
.footer .brand{left:140px;top:76px;font-size:34px;color:#fff}
.footer .brand .mark{background:#fff}
.f-desc{position:absolute;left:138px;top:145px;width:250px;font-size:12px;line-height:19px;color:#e3eeec}
.social{position:absolute;top:220px;width:24px;height:24px;border:2px solid var(--mint-soft);border-radius:50%}
.f-col{position:absolute;top:84px}
.f-col h5{font-family:"Poppins",Arial,sans-serif;font-weight:600;font-size:17px;color:#fff}
.f-col .rule{width:150px;height:1px;background:rgba(255,255,255,.35);margin:8px 0 14px}
.f-col a{display:block;font-size:12.5px;color:#e3eeec;text-decoration:none;line-height:27px}
.c-item{position:absolute;left:848px;display:flex;gap:14px;align-items:flex-start;font-size:12.5px;line-height:17px;color:#e3eeec}
.c-ico{width:26px;height:26px;border-radius:50%;background:var(--mint-soft);flex:none;display:flex;align-items:center;justify-content:center}
.f-rule{position:absolute;left:126px;top:362px;width:970px;height:1px;background:rgba(255,255,255,.25)}
.f-small{position:absolute;top:389px;font-size:12px;color:#e3eeec}
</style>
</head>
<body>

<!-- HERO -->
<section class="hero">
  <div class="brand site-brand"><span class="mark"></span>belmorin</div>
  <a class="nav-link" style="left:411px">Platform</a>
  <a class="nav-link" style="left:512px">Cyber Risk</a>
  <a class="nav-link" style="left:627px">AI Risk</a>
  <a class="nav-link" style="left:714px">Company</a>
  <a class="nav-link" style="left:822px">About Us</a>
  <a class="nav-link" style="left:931px">Team</a>
  <div class="btn-nav">Contact <span class="tri" style="border-left-width:5px;border-right-width:5px;border-top-width:8px"></span></div>

  <h1 class="abs hero-title">Cyber Insurance the<br><span class="accent">Way It Should Be</span></h1>
  <p class="abs hero-sub">Evidence based, automation driven<br>underwriting for the AI era</p>
  <div class="btn" style="left:119px;top:446px;width:174px;height:47px">Contact Us <span class="tri"></span></div>

  <div class="abs hero-art" role="img" aria-label="Illustration of cybersecurity data being distilled into the Belmorin platform"></div>
  <div class="tag" style="left:1027px;top:236px">Cybersecurity Data</div>
  <div class="tag" style="left:601px;top:354px;width:145px">Distilled</div>
  <div class="tag" style="left:904px;top:458px">Belmorin Platform</div>
  <div class="tag" style="left:598px;top:528px;font-size:12px">Represents Data Distillation<br>into actionableintelligence</div>
</section>

<!-- DIFFERENT -->
<h2 class="sec-title" style="top:813px">What Makes <span class="accent">Belmorin Different</span></h2>
<div class="underline" style="top:864px"></div>

<svg class="abs" style="left:0;top:980px" width="1200" height="1000" viewBox="0 0 1200 1000" fill="none" aria-hidden="true">
  <line x1="962" y1="65" x2="1200" y2="65" stroke="var(--line)" stroke-width="1.5"/>
  <circle cx="960" cy="65" r="3.5" fill="var(--mint)"/>
  <path d="M680 330 C680 370 640 380 560 385 C520 388 502 400 502 430" stroke="var(--line)" stroke-width="2"/>
  <line x1="0" y1="490" x2="130" y2="490" stroke="var(--line)" stroke-width="1.5"/>
  <circle cx="132" cy="490" r="3.5" fill="var(--mint)"/>
  <path d="M502 775 C502 810 540 820 620 822 C660 824 678 835 678 850" stroke="var(--line)" stroke-width="2"/>
  <line x1="942" y1="990" x2="1200" y2="990" stroke="var(--line)" stroke-width="1.5"/>
  <circle cx="940" cy="990" r="3.5" fill="var(--mint)"/>
</svg>

<!-- feature 1 -->
<div class="art" style="left:132px;top:917px;width:463px;height:405px;background:radial-gradient(ellipse 130px 90px at 50% 22%,rgba(15,61,59,.8),transparent 80%),radial-gradient(ellipse 240px 110px at 50% 72%,rgba(60,80,240,.35),transparent 80%)" role="img" aria-label="Isometric illustration of the Belmorin platform hub above a dashboard"></div>
<h3 class="f-title" style="left:665px;top:985px">End to End Cyber Risk and<br>Insurance Platform</h3>
<div class="f-bar" style="left:665px;top:1064px"></div>
<p class="f-text" style="left:665px;top:1080px;width:420px">The Belmorin platform streamlines the entire policy lifecycle, incentivizes and empowers policyholders to actively reduce their risk, and elevates brokers as trusted advisors.</p>
<div class="btn" style="left:664px;top:1231px;width:172px;height:47px">Learn More <span class="tri"></span></div>

<!-- feature 2 -->
<h3 class="f-title" style="left:164px;top:1448px">Proprietary Tools and<br>Rapid Response</h3>
<div class="f-bar" style="left:164px;top:1534px"></div>
<p class="f-text" style="left:164px;top:1547px;width:400px">Advanced security tools and 24/7 incident response capabilities protect businesses before, during, and after cyber events.</p>
<div class="btn" style="left:162px;top:1675px;width:173px;height:47px">Learn More <span class="tri"></span></div>
<div class="art" style="left:620px;top:1405px;width:520px;height:372px;background:radial-gradient(ellipse 140px 80px at 50% 50%,rgba(47,111,200,.75),transparent 80%),radial-gradient(ellipse 260px 170px at 50% 50%,rgba(150,230,205,.45),transparent 80%)" role="img" aria-label="Isometric illustration of a security operations dashboard surrounded by analysts"></div>

<!-- feature 3 -->
<div class="art" style="left:83px;top:1843px;width:545px;height:422px;background:radial-gradient(ellipse 160px 120px at 55% 45%,rgba(170,175,245,.6),transparent 80%),radial-gradient(ellipse 270px 130px at 50% 72%,rgba(150,230,205,.45),transparent 80%)" role="img" aria-label="Isometric illustration of charts and reports on a laptop platform"></div>
<h3 class="f-title" style="left:643px;top:1920px">Insurance DNA and<br>Tech Execution</h3>
<div class="f-bar" style="left:643px;top:1998px"></div>
<p class="f-text" style="left:643px;top:2012px;width:450px">Founded by a team with deep expertise in cyber insurance and cybersecurity, we understand both the risk landscape and the insurance market.</p>
<div class="btn" style="left:643px;top:2136px;width:174px;height:46px">Learn More <span class="tri"></span></div>

<!-- LIFECYCLE -->
<section class="lifecycle"></section>
<div class="floor" role="img" aria-label="Perspective grid floor"></div>
<h2 class="sec-title" style="top:2491px">The Complete Cyber <span class="accent">Insurance Lifecycle</span></h2>
<div class="underline" style="top:2542px"></div>

<svg class="abs" style="left:0;top:2600px" width="1200" height="200" viewBox="0 0 1200 200" aria-hidden="true">
  <defs>
    <linearGradient id="g1" x1="0" y1="0" x2="1" y2="1"><stop offset="0" stop-color="#0f3d3b"/><stop offset="1" stop-color="#134c48"/></linearGradient>
    <linearGradient id="g2" x1="0" y1="0" x2="1" y2="1"><stop offset="0" stop-color="#2a7a68"/><stop offset="1" stop-color="#5fc8a0"/></linearGradient>
    <linearGradient id="g3" x1="0" y1="0" x2="1" y2="1"><stop offset="0" stop-color="#7fe3c4"/><stop offset="1" stop-color="#4fc8b4"/></linearGradient>
    <linearGradient id="g4" x1="0" y1="0" x2="1" y2="1"><stop offset="0" stop-color="#5fb8e8"/><stop offset="1" stop-color="#3650e8"/></linearGradient>
    <linearGradient id="g5" x1="0" y1="0" x2="1" y2="1"><stop offset="0" stop-color="#2a2af0"/><stop offset="1" stop-color="#1a14c8"/></linearGradient>
  </defs>
  <g fill="none" stroke-width="2.5">
    <path d="M248 25 A74 74 0 0 0 175 110" stroke="#0f3d3b"/><path d="M248 25 A74 74 0 0 1 322 99" stroke="#0f3d3b" stroke-dasharray="3 6"/>
    <path d="M425 25 A74 74 0 0 0 352 110" stroke="#2a7a68"/><path d="M425 173 A74 74 0 0 0 499 99" stroke="#5fc8a0" stroke-dasharray="3 6"/>
    <path d="M602 25 A74 74 0 0 0 529 110" stroke="#5fdcb4"/><path d="M602 173 A74 74 0 0 0 676 99" stroke="#5fdcb4" stroke-dasharray="3 6"/>
    <path d="M780 25 A74 74 0 0 0 707 110" stroke="#3f9ae0"/><path d="M780 173 A74 74 0 0 0 854 99" stroke="#3650e8" stroke-dasharray="3 6"/>
    <path d="M959 25 A74 74 0 0 0 886 110" stroke="#2a2af0"/><path d="M959 173 A74 74 0 0 0 1033 99" stroke="#2a2af0" stroke-dasharray="3 6"/>
  </g>
  <circle cx="248" cy="99" r="56" fill="url(#g1)"/>
  <circle cx="425" cy="99" r="56" fill="url(#g2)"/>
  <circle cx="602" cy="99" r="56" fill="url(#g3)"/>
  <circle cx="780" cy="99" r="56" fill="url(#g4)"/>
  <circle cx="959" cy="99" r="56" fill="url(#g5)"/>
  <g fill="none" stroke="#fff" stroke-width="2.5" stroke-linecap="round" stroke-linejoin="round">
    <circle cx="248" cy="99" r="20"/><path d="M238 99 l7 7 l13 -14"/>
    <rect x="408" y="84" width="34" height="28" rx="3"/><path d="M414 93 h22 M414 101 h14"/>
    <path d="M586 104 q16 14 32 0 M594 88 a8 8 0 1 0 16 0 a8 8 0 1 0 -16 0"/>
    <circle cx="780" cy="99" r="12"/><path d="M780 79 v8 M780 111 v8 M760 99 h8 M792 99 h8"/>
    <rect x="946" y="80" width="26" height="36" rx="3"/><path d="M952 90 h14 M952 98 h14 M952 106 h9"/>
  </g>
  <g font-family="Inter,Arial,sans-serif" font-size="11" font-weight="600" fill="#fff" text-anchor="middle">
    <circle cx="199" cy="160" r="10" fill="#0f3d3b"/><text x="199" y="164">1</text>
    <circle cx="378" cy="160" r="10" fill="#0f3d3b"/><text x="378" y="164">2</text>
    <circle cx="549" cy="160" r="10" fill="#0f3d3b"/><text x="549" y="164">3</text>
    <circle cx="726" cy="160" r="10" fill="#0f3d3b"/><text x="726" y="164">4</text>
    <circle cx="902" cy="160" r="10" fill="#0f3d3b"/><text x="902" y="164">5</text>
  </g>
</svg>

<div class="step" style="left:167px;top:2818px"><h3>ENSURE</h3><p>Best in class cyber insurance coverage with comprehensive first and third party protections</p></div>
<div class="step" style="left:349px;top:2818px"><h3>ASSESS</h3><p>Dynamic scanning and read-only API integrations to continuously evaluate risk posture and inform underwriting</p></div>
<div class="step" style="left:528px;top:2818px"><h3>IMPROVE</h3><p>Incentivize and guide policyholders to actively strengthen their cybersecurity through behavior rewards</p></div>
<div class="step" style="left:709px;top:2818px"><h3>REMEDIATE</h3><p>Expert post-breach services including forensics, restoration, and crisis management support</p></div>
<div class="step" style="left:893px;top:2818px"><h3>RENEW</h3><p>Seamless policy renewals with transparent pricing based on demonstrated risk improvements</p></div>

<!-- INTEGRATIONS -->
<section class="integrations"></section>
<h2 class="sec-title" style="top:3158px">Seamlessly Integrates With<br><span class="accent">Your Tech Stack</span></h2>
<div class="underline" style="top:3251px"></div>

<div class="tab active" style="top:3357px">Identity Platforms</div>
<div class="tab" style="top:3431px">Developer Platforms</div>
<div class="tab" style="top:3504px">Endpoint Security</div>
<div class="tab" style="top:3578px">Cloud Infrastructure</div>

<div class="int-card">
  <h4>Identity Platforms</h4>
  <div class="logo-box" style="left:34px">Gridlane Suite</div>
  <div class="logo-box" style="left:238px">Keystride</div>
  <div class="logo-box" style="left:442px">Cobalt Directory</div>
</div>

<!-- FOOTER -->
<footer class="footer">
  <div class="brand"><span class="mark"></span>belmorin</div>
  <p class="f-desc">Reducing the frequency and severity of cyber risk by strengthening organizations' cyber risk posture.</p>
  <span class="social" style="left:138px"></span>
  <span class="social" style="left:172px"></span>
  <span class="social" style="left:206px"></span>

  <div class="f-col" style="left:476px">
    <h5>Navigation</h5><div class="rule"></div>
    <a>Platform</a><a>Cyber Risk</a><a>AI Risk</a><a>Company</a><a>About Us</a>
  </div>
  <div class="f-col" style="left:661px">
    <h5>Resources</h5><div class="rule"></div>
    <a>Team</a><a>How it Works</a><a>The Problem</a><a>The Solution</a><a>Contact</a>
  </div>
  <div class="f-col" style="left:848px">
    <h5>Contact Us</h5><div class="rule" style="width:180px"></div>
  </div>

  <div class="c-item" style="top:117px">
    <span class="c-ico"><svg width="14" height="14" viewBox="0 0 24 24" fill="var(--footer)"><path d="M6.6 10.8a15 15 0 0 0 6.6 6.6l2.2-2.2a1 1 0 0 1 1-.25 11.4 11.4 0 0 0 3.6.6 1 1 0 0 1 1 1V20a1 1 0 0 1-1 1A17 17 0 0 1 3 4a1 1 0 0 1 1-1h3.5a1 1 0 0 1 1 1c0 1.25.2 2.45.6 3.6a1 1 0 0 1-.25 1z"/></svg></span>
    <span>Phone Number<br>(555) 014-2290</span>
  </div>
  <div class="c-item" style="top:174px">
    <span class="c-ico"><svg width="14" height="14" viewBox="0 0 24 24" fill="none" stroke="var(--footer)" stroke-width="2.4"><rect x="3" y="5" width="18" height="14" rx="2"/><path d="M3 7l9 6 9-6"/></svg></span>
    <span>Email address<br>info@belmorin-cover.test</span>
  </div>
  <div class="c-item" style="top:230px">
    <span class="c-ico"><svg width="14" height="14" viewBox="0 0 24 24" fill="var(--footer)"><path d="M12 2a7 7 0 0 0-7 7c0 5 7 13 7 13s7-8 7-13a7 7 0 0 0-7-7zm0 9.5A2.5 2.5 0 1 1 12 6.5a2.5 2.5 0 0 1 0 5z"/></svg></span>
    <span>2nd Floor 410 Larkspur Avenue,<br>00000 Fairhollow NJ</span>
  </div>

  <div class="f-rule"></div>
  <p class="f-small" style="left:127px">Copyright © 2026 Belmorin. All Right Reserved</p>
  <p class="f-small" style="left:852px">Privacy Policy</p>
  <p class="f-small" style="left:959px">Terms and Conditions</p>
</footer>

</body>
</html>
```